Request for Business Card Design

Hi. My name is Marlena, I am looking for a new business card design for my company, Quillbrook Sensing Systems, LLC. I really like the design you did for Tavel Harvest and was hoping you could do something similar using our full logo and our mark. I am also open to any raised texture design using our mark. I have attached our full logo, which would need to be somewhere on the card, as well as the mark in both outline and full form, as well as our brand colors / guide. The card does not have to be white, as long as our logo and mark appear. I actually like darker colored business cards more, but am open to all options. If you are interested in working with me, please let me know. We would also take the business card design into letterhead design if you can do that.

```html
<!DOCTYPE html>
<html lang="en">
<head>
<meta charset="utf-8">
<title>Quillbrook Sensing Systems — Business Card</title>
<link href="https://fonts.googleapis.com/css2?family=Lato:wght@400;700;900&display=swap" rel="stylesheet">
<style>
  :root {
    --stage: #2b2d31;
    --card: #ffffff;
    --brand-blue: #0796bf;
    --ink: #1f1f21;
    --ink-soft: #3d3d40;
    --rule-dark: #2a2a2c;
  }
  html, body {
    margin: 0;
    width: 1200px;
    height: 952px;
    overflow: hidden;
    background: var(--stage);
    font-family: "Lato", sans-serif;
  }
  .stage {
    width: 1200px;
    height: 952px;
    display: flex;
    align-items: center;
    justify-content: center;
  }
  .business-card {
    position: relative;
    width: 900px;
    height: 520px;
    background: var(--card);
    border-radius: 34px;
    overflow: hidden;
    box-shadow: 0 18px 40px rgba(0,0,0,0.35);
  }
  .brand-lockup {
    position: absolute;
    left: 120px;
    top: 150px;
    width: 300px;
    display: flex;
    align-items: center;
    gap: 18px;
  }
  .brand-dot {
    flex: none;
    width: 46px;
    height: 46px;
    border-radius: 50%;
    background: var(--brand-blue);
  }
  .brand-name {
    color: var(--brand-blue);
    font-weight: 900;
    font-size: 34px;
    line-height: 1.1;
    letter-spacing: 0.5px;
  }
  .identity {
    position: absolute;
    left: 485px;
    top: 150px;
  }
  .person-name {
    margin: 0;
    font-size: 30px;
    font-weight: 400;
    letter-spacing: 1.5px;
    color: var(--ink);
    text-transform: uppercase;
  }
  .person-name .surname {
    color: var(--brand-blue);
    font-weight: 900;
  }
  .person-role {
    margin: 4px 0 0;
    font-size: 20px;
    color: var(--ink-soft);
    letter-spacing: 0.4px;
  }
  .name-rule {
    width: 52px;
    height: 2px;
    background: var(--rule-dark);
    margin: 14px 0 16px;
  }
  .contact-list {
    list-style: none;
    margin: 0;
    padding: 0;
  }
  .contact-item {
    display: flex;
    align-items: flex-start;
    gap: 12px;
    font-size: 17px;
    line-height: 1.3;
    color: var(--ink-soft);
    margin-bottom: 8px;
  }
  .contact-icon {
    flex: none;
    width: 22px;
    height: 22px;
    border-radius: 4px;
    display: flex;
    align-items: center;
    justify-content: center;
    background: var(--brand-blue);
  }
  .contact-icon.is-dark { background: var(--ink); }
  .edge-rule-dark {
    position: absolute;
    left: 0;
    bottom: 26px;
    width: 395px;
    height: 3px;
    background: var(--rule-dark);
  }
  .edge-rule-blue {
    position: absolute;
    left: 402px;
    right: 0;
    bottom: 24px;
    height: 7px;
    background: var(--brand-blue);
  }
</style>
</head>
<body>
<main class="stage">
  <article class="business-card">
    <div class="brand-lockup">
      <span class="brand-dot"></span>
      <span class="brand-name">Quillbrook Sensing Systems</span>
    </div>

    <section class="identity">
      <h1 class="person-name">Dorian K. <span class="surname">Ashvale</span></h1>
      <p class="person-role">Managing Director</p>
      <div class="name-rule"></div>
      <ul class="contact-list">
        <li class="contact-item">
          <span class="contact-icon is-dark">
            <svg width="12" height="14" viewBox="0 0 12 14"><path d="M6 0a5 5 0 0 0-5 5c0 3.6 5 9 5 9s5-5.4 5-9a5 5 0 0 0-5-5z" fill="#fff"/><circle cx="6" cy="5" r="2" fill="#1f1f21"/></svg>
          </span>
          <span>2117 Larchmont Avenue<br>Fairhaven, OR 97402</span>
        </li>
        <li class="contact-item">
          <span class="contact-icon">
            <svg width="13" height="13" viewBox="0 0 13 13"><path d="M2.5 0.8l2 2.6-1.2 1.6c0.8 1.8 2 3 3.8 3.8l1.6-1.2 2.6 2-1 2.4C5.6 12 1 7.4 0.1 2z" fill="#fff"/></svg>
          </span>
          <span>+00 987 654 32</span>
        </li>
        <li class="contact-item">
          <span class="contact-icon">
            <svg width="14" height="10" viewBox="0 0 14 10"><rect x="0.5" y="0.5" width="13" height="9" fill="none" stroke="#fff"/><path d="M0.5 0.5l6.5 5 6.5-5" fill="none" stroke="#fff"/></svg>
          </span>
          <span>hello@quillbrooksensing.com</span>
        </li>
        <li class="contact-item">
          <span class="contact-icon">
            <svg width="12" height="12" viewBox="0 0 12 12"><path d="M6 0l5 11-5-3-5 3z" fill="#fff"/></svg>
          </span>
          <span>www.quillbrooksensing.com</span>
        </li>
      </ul>
    </section>

    <div class="edge-rule-dark"></div>
    <div class="edge-rule-blue"></div>
  </article>
</main>
</body>
</html>
```